Property Developer - Simple yet Sophisticated and Sharp Business Card

We are a medium sized property developer involved mainly in townhouse developments and land subdivisions.

The company is looking for a simple, sharp and sophisticated business card that will be given to contractors, land owners, financiers etc and thus will need to look professional.

Property development related graphics and art can be used, however the card is not to be too "busy" or crowded. Our company name is KL Estates which could possibly be incorporated into the graphics or artwork.

Single sided and/or double sided designs will be acceptable.

A Simple, Sophisticated, Sharp design please!

Good Luck !

```html
<!DOCTYPE html>
<html lang="en">
<head>
<meta charset="utf-8">
<title>KL Estates – Business Card</title>
<link rel="stylesheet" href="https://fonts.googleapis.com/css2?family=Open+Sans:wght@400;700;800&display=swap">
<style>
  :root {
    --page-bg: #e9e9e9;
    --card-dark: #231f20;
    --card-light: #ffffff;
    --accent: #f0a824;
    --text-light: #ffffff;
    --text-dark: #231f20;
  }
  * { margin: 0; padding: 0; box-sizing: border-box; }
  html, body {
    width: 1200px;
    height: 951px;
    overflow: hidden;
    background: var(--page-bg);
    font-family: "Open Sans", Arial, sans-serif;
  }
  .canvas {
    position: relative;
    width: 1200px;
    height: 951px;
  }
  .card {
    position: absolute;
    width: 620px;
    height: 378px;
    border-radius: 26px;
    overflow: hidden;
    box-shadow: 0 10px 28px rgba(0,0,0,0.25);
  }
  .card-front {
    left: 90px;
    top: 90px;
    background: var(--card-dark);
    display: flex;
    align-items: center;
    justify-content: center;
  }
  .brand-name {
    font-weight: 800;
    letter-spacing: 0.5px;
    white-space: nowrap;
  }
  .card-front .brand-name {
    font-size: 64px;
    color: var(--text-light);
  }
  .card-back {
    left: 490px;
    top: 483px;
    background: var(--card-light);
  }
  .card-back .panel-shape {
    position: absolute;
    inset: 0;
    width: 100%;
    height: 100%;
  }
  .card-back .brand-name {
    position: absolute;
    left: 34px;
    top: 160px;
    font-size: 38px;
    color: var(--text-dark);
  }
  .contact {
    position: absolute;
    left: 310px;
    top: 92px;
    color: var(--text-light);
    font-size: 15px;
    line-height: 1.32;
  }
  .contact-name {
    color: var(--accent);
    font-size: 19px;
  }
  .contact-role {
    font-size: 15px;
    margin-bottom: 26px;
  }
</style>
</head>
<body>
<main class="canvas">
  <section class="card card-front">
    <span class="brand-name">KL Estates</span>
  </section>

  <section class="card card-back">
    <svg class="panel-shape" viewBox="0 0 620 378" preserveAspectRatio="none" aria-hidden="true">
      <path d="M290 0 C255 90 255 150 270 200 C285 260 285 320 265 378 L620 378 L620 0 Z" fill="var(--card-dark)"/>
      <path d="M290 0 C255 90 255 150 270 200 C285 260 285 320 265 378" fill="none" stroke="var(--accent)" stroke-width="4"/>
    </svg>
    <span class="brand-name">KL Estates</span>
    <div class="contact">
      <p class="contact-name">Mark Hallworth</p>
      <p class="contact-role">Administration</p>
      <p>PO Box 2245 Eastwood,</p>
      <p>North QLD 4215</p>
      <p>P: (07) 3208 5514</p>
      <p>F: (07) 3296 4471</p>
      <p>E: projects.klestates@mailbox.com</p>
    </div>
  </section>
</main>
</body>
</html>
```